Dedicated publishing company needs Book Cover with heart and soul

I am looking for a book cover design for a lovestory named "Kellnerinnen tanzen leiser" which means "waitresses dance quieter". It´s a funny, smart and heartwarming lovestory about a couple that seems to be too diverse - but which is meant to be.
He is a young and handsome movie star and she is the interior decorator of his film sets - an "average" looking slightly older woman with the heart in the right place.
Maybe some frames to reflect her work would be nice or some hollywood decor?
We are a dedicated publishing company who cares not only for the content but also for the design and we are open to any ideas! Looking forward to seeing your designs!

Target Market(s)

Women who enjoy good love stories

Industry/Entity Type

Publishing Company

Requirements
Must have
• The title: Kellnerinnen tanzen leiser
The autors name: Petra Lindqvist

Size of front 14,8 cm wide / 21 cm high ( with additional 3 mm around), spine approx 3 cm.
Front and back design

```html
<!DOCTYPE html>
<html lang="de">
<head>
<meta charset="utf-8">
<title>Kellnerinnen tanzen leiser – Petra Lindqvist</title>
<link rel="stylesheet" href="https://fonts.googleapis.com/css2?family=Parisienne&family=Oranienbaum&display=swap">
<style>
  :root {
    --ink-black: #0a0205;
    --deep-maroon: #3c0612;
    --wine: #6a0a24;
    --magenta: #c8125a;
    --hot-pink: #e23a78;
    --ember-red: #ee4a3a;
    --glow-orange: #f4a53c;
    --glow-yellow: #f8c85a;
    --title-white: #ffffff;
    --author-gold: #f5a43a;
  }
  html, body {
    margin: 0;
    padding: 0;
    width: 795px;
    height: 1200px;
    overflow: hidden;
    background: var(--ink-black);
  }
  .cover {
    position: relative;
    width: 795px;
    height: 1200px;
    overflow: hidden;
  }
  .cover-artwork {
    position: absolute;
    inset: 0;
    background:
      /* warm glow across the upper centre */
      radial-gradient(ellipse 200px 170px at 400px 120px, var(--glow-yellow) 0%, var(--glow-orange) 50%, rgba(238,74,58,0.6) 80%, transparent 100%),
      /* small warm accent upper right */
      radial-gradient(ellipse 70px 60px at 620px 280px, var(--glow-orange) 0%, transparent 100%),
      /* glowing highlights along the rising band */
      radial-gradient(ellipse 210px 90px at 560px 470px, var(--glow-orange) 0%, rgba(244,165,60,0.7) 50%, transparent 100%),
      radial-gradient(ellipse 220px 150px at 170px 720px, var(--glow-yellow) 0%, var(--glow-orange) 45%, rgba(226,58,120,0.6) 80%, transparent 100%),
      radial-gradient(ellipse 110px 140px at 420px 700px, rgba(238,74,58,0.55) 0%, transparent 100%),
      /* dark shadow mass on the left */
      radial-gradient(ellipse 260px 320px at 60px 360px, var(--ink-black) 0%, rgba(10,2,5,0.85) 55%, transparent 100%),
      /* diagonal structure: dark top, magenta band, black stripe, magenta base */
      linear-gradient(142deg,
        var(--deep-maroon) 0%,
        var(--wine) 24%,
        var(--deep-maroon) 30%,
        var(--magenta) 38%,
        var(--hot-pink) 46%,
        var(--magenta) 57%,
        var(--ink-black) 61%,
        var(--ink-black) 65%,
        var(--magenta) 71%,
        var(--magenta) 100%);
  }
  .cover-title {
    position: absolute;
    left: 0;
    top: 920px;
    width: 795px;
    height: 90px;
    margin: 0;
  }
  .cover-title text {
    font-family: "Parisienne", cursive;
    font-size: 68px;
    fill: var(--title-white);
  }
  .cover-author {
    position: absolute;
    left: 0;
    top: 1050px;
    width: 795px;
    height: 110px;
  }
  .cover-author text {
    font-family: "Oranienbaum", serif;
    font-size: 106px;
    fill: var(--author-gold);
    stroke: var(--author-gold);
    stroke-width: 1.6px;
  }
</style>
</head>
<body>
  <main class="cover">
    <div class="cover-artwork" role="img" aria-label="Posterised close-up illustration of a film star and a woman about to kiss, glowing magenta, orange and black"></div>
    <svg class="cover-title" viewBox="0 0 795 90" role="heading" aria-level="1" aria-label="Kellnerinnen tanzen leiser">
      <text x="38" y="62" textLength="728" lengthAdjust="spacingAndGlyphs">“Kellnerinnen tanzen leiser”</text>
    </svg>
    <svg class="cover-author" viewBox="0 0 795 110" aria-label="Petra Lindqvist">
      <text x="72" y="92" textLength="684" lengthAdjust="spacingAndGlyphs">PETRA LINDQVIST</text>
    </svg>
  </main>
</body>
</html>
```